PebbleTrustLending.com

We are setting up a new company to make small business loans over the internet. We have a logo. Customers will apply on line, so the online application must allow customers to upload files.

We need a complete design and also a some who can build the online application and website for us (CODING). When applicants fill out fields, at various points they may be able to move to the next questions or receive a notice that their application is not eligible for funding.

Sample sites are: MarbleHarbor.com/us, RovenTide.com, Quillory.com, ByNest.com, JuvaCredit.com, plumebridge.com, tollivan.com.

We think WordPress makes the most sense but we are open to suggestions.

Note, we will request that the winning designer build the site for us including the online application. We will negotiate this separately, I presume, before we pick the final winner.

Target Market(s)

Small businesses in the United States.

Industry/Entity Type

Small Business

Requirements
Must have
• Online application - fields and ability to upload basic files.

https://filevault.example-share.net/redir?resid=A48D2EF7C1B0E93!51827&authkey=!QZtRmW284pXkvNe&ithint=file,.pdf

```html
<!DOCTYPE html>
<html lang="en">
<head>
<meta charset="utf-8">
<title>PebbleTrustLending – Online Business Loans</title>
<link rel="stylesheet" href="https://fonts.googleapis.com/css2?family=Open+Sans:ital,wght@0,400;0,600;0,700;1,400&display=swap">
<style>
:root{
  --teal:#1d5275;
  --teal-dark:#133f5c;
  --nav:#1b4a66;
  --orange:#e8531f;
  --orange-light:#ff6a2a;
  --text:#555;
  --text-light:#777;
  --heading:#444;
  --card-border:#dcdcdc;
  --footer-top:#2a6c8e;
  --footer-bottom:#0f3a5c;
}
*{box-sizing:border-box;margin:0;padding:0}
html,body{width:1200px;height:2332px;overflow:hidden;background:#fff}
body{font-family:"Open Sans",Arial,sans-serif;color:var(--text);position:relative}

/* header */
.site-header{position:absolute;left:0;top:0;width:1200px;height:112px;background:#fff}
.brand{position:absolute;left:65px;top:30px;display:flex;align-items:center;gap:10px}
.brand-dot{width:52px;height:52px;border-radius:50%;background:var(--orange)}
.brand-name{font-weight:700;font-size:26px;color:var(--teal-dark);letter-spacing:-.5px;white-space:nowrap}
.main-nav{position:absolute;top:52px;left:448px;width:680px;display:flex;justify-content:space-between}
.main-nav a{font-size:17px;font-weight:600;color:var(--nav);text-decoration:none;white-space:nowrap}

/* hero */
.hero{position:absolute;left:0;top:112px;width:1200px;height:472px;background:linear-gradient(100deg,#8d8170 0%,#c9bca8 35%,#d9d3cc 60%,#b5533a 85%,#9c4430 100%)}
.hero-caption{position:absolute;left:71px;top:149px;width:509px;height:186px;background:rgba(22,78,108,.86);padding:20px 30px 0 34px;color:#fff;overflow:hidden}
.hero-caption h1{font-weight:400;font-size:36px;line-height:44px;white-space:nowrap}
.hero-caption h2{font-weight:400;font-size:25px;line-height:32px;margin-top:2px;white-space:nowrap}
.hero-caption p{font-size:13px;line-height:21px;margin-top:10px;color:#e6eef3}
.slider-dots{position:absolute;left:566px;top:446px;display:flex;gap:6px}
.slider-dots span{width:13px;height:13px;border-radius:50%;background:#8a8a8a}
.slider-dots span.active{background:#1e1e1e}

/* how it works */
.section-title{position:absolute;width:1200px;text-align:center;font-weight:400;font-size:37px;color:var(--heading)}
.intro{position:absolute;left:135px;top:668px;width:930px;text-align:center;font-size:15px;line-height:24px;color:#666}
.step{position:absolute;top:755px;width:344px;height:325px;border:1px solid var(--card-border);border-radius:3px;background:linear-gradient(#fff 72%,#eee);text-align:center}
.step svg{margin-top:30px}
.step h3{font-weight:400;font-size:26px;color:var(--orange);margin-top:14px}
.step p{font-size:13.5px;line-height:23px;color:var(--text-light);margin:6px 44px 0}
.btn-read{display:inline-block;margin-top:18px;width:131px;height:32px;line-height:32px;border-radius:16px;background:linear-gradient(#24597c,#0f3957);color:#fff;font-size:14px;font-weight:600}

/* featured */
.featured-row{position:absolute;left:148px;top:1172px;width:906px;display:flex;justify-content:space-between}
.featured-badge{width:125px;height:48px;background:#8b8b8b;border-radius:4px;opacity:.75}
.divider{position:absolute;left:60px;width:1080px;height:30px;background:radial-gradient(ellipse at center top,rgba(0,0,0,.07),rgba(0,0,0,0) 70%)}

/* about */
.about{position:absolute;left:65px;top:1300px;width:580px}
.about h2{font-weight:400;font-size:33px;color:var(--teal)}
.about .lead{font-size:18.5px;line-height:25px;color:#555;margin-top:12px}
.about p{font-size:14px;line-height:23px;color:#666;margin-top:12px}
.btn-start{position:absolute;left:62px;top:1574px;width:183px;height:42px;border-radius:21px;background:linear-gradient(var(--orange-light),#e8430f);color:#fff;font-weight:600;font-size:19px;text-align:center;line-height:42px}
.video-title{position:absolute;left:693px;top:1300px;font-weight:400;font-size:33px;color:var(--orange)}
.video{position:absolute;left:695px;top:1352px;width:433px;height:264px;border:1px solid #ccc;background:linear-gradient(120deg,#d7dadd,#5b6672 45%,#2d3440 70%,#b9a79a)}
.video svg{position:absolute;left:0;top:0}

/* testimonials */
.testimonial{position:absolute;top:1806px;width:520px}
.avatar{position:absolute;left:0;top:0;width:96px;height:96px;border-radius:50%;background:linear-gradient(#5b7d9a,#2f4f6c);box-shadow:0 8px 6px -6px rgba(0,0,0,.25)}
.quote{position:absolute;left:107px;top:4px;width:410px;font-style:italic;font-size:14.5px;line-height:23px;color:#555}
.author{position:absolute;left:107px;top:104px;font-size:15px;color:#555}

/* footer */
.site-footer{position:absolute;left:0;top:1986px;width:1200px;height:346px;background:linear-gradient(var(--footer-top),var(--footer-bottom));border-top:1px dashed rgba(255,255,255,.45);color:#fff}
.footer-col{position:absolute;top:44px}
.footer-col h4{font-weight:400;font-size:23px;margin-bottom:8px}
.footer-col li{list-style:none;font-size:14px;line-height:25px}
.footer-col .note{font-size:13px;color:#b7cbd8}
.social{display:flex;gap:5px;margin-top:10px}
.social span{width:34px;height:34px;border-radius:50%;background:#fff}
.copyright{position:absolute;left:78px;top:305px;font-size:13.5px;color:#b7cbd8}
</style>
</head>
<body>

<header class="site-header">
  <div class="brand"><span class="brand-dot"></span><span class="brand-name">PebbleTrustLending</span></div>
  <nav class="main-nav">
    <a href="#">About Us</a><a href="#">Online Loans</a><a href="#">Howit Works</a><a href="#">Testimonials</a><a href="#">Get Started</a><a href="#">Contact</a>
  </nav>
</header>

<section class="hero" role="img" aria-label="Photo of a woman on a sofa working on a laptop">
  <div class="hero-caption">
    <h1>Online Business Loans</h1>
    <h2>We Provide loans for Small Business</h2>
    <p>Class aptent taciti sociosqu ad litora torquent per conubia nostra, per inceptos hymenaeos. Proin nulla arcu, nonummy luctus</p>
  </div>
  <div class="slider-dots"><span class="active"></span><span></span><span></span><span></span></div>
</section>

<h2 class="section-title" style="top:612px">How it Works</h2>
<p class="intro">Duis tincidunt lectus quis dui viverra vestibulum. Suspendisse vulputate aliquam dui. Nulla elementum dui ut augue. Aliquam vehicula mi at mauris. Maecenas placerat, nisl at consequat rhoncus, sem nunc gravida justo, quis eleifend arcu velit quis lacus.</p>

<div class="step" style="left:64px">
  <svg width="96" height="96" viewBox="0 0 96 96" fill="none" stroke="#e8531f" stroke-width="5">
    <path d="M18 8h44l16 16v64H18z"/><path d="M62 8v16h16"/>
    <path d="M28 40h30M28 52h40M28 64h40M28 76h26"/>
  </svg>
  <h3>Cras elit Integer</h3>
  <p>Class aptent taciti sociosqu ad litora torquent per conubia nostra, per inceptos hymenaeos Proin nulla arcu</p>
  <span class="btn-read">Read More</span>
</div>

<div class="step" style="left:424px">
  <svg width="96" height="96" viewBox="0 0 96 96">
    <rect x="20" y="34" width="68" height="56" fill="#e8531f"/>
    <g fill="#fff"><rect x="48" y="48" width="10" height="8"/><rect x="62" y="48" width="10" height="8"/><rect x="34" y="62" width="10" height="8"/><rect x="48" y="62" width="10" height="8"/><rect x="62" y="62" width="10" height="8"/><rect x="34" y="76" width="10" height="8"/><rect x="48" y="76" width="10" height="8"/><rect x="62" y="76" width="10" height="8"/></g>
    <circle cx="30" cy="30" r="24" fill="#fff" stroke="#e8531f" stroke-width="5"/>
    <path d="M30 16v14h10" stroke="#e8531f" stroke-width="4" fill="none"/>
  </svg>
  <h3>Pellentesque faucibus</h3>
  <p>Class aptent taciti sociosqu ad litora torquent per conubia nostra, per inceptos hymenaeos Proin nulla arcu</p>
  <span class="btn-read">Read More</span>
</div>

<div class="step" style="left:786px">
  <svg width="96" height="96" viewBox="0 0 96 96">
    <rect x="40" y="6" width="30" height="50" rx="3" fill="#e8531f" transform="rotate(-12 55 31)"/>
    <circle cx="55" cy="30" r="7" fill="#fff"/>
    <rect x="10" y="48" width="14" height="38" fill="#e8531f"/>
    <path d="M28 50h34a8 8 0 0 1 8 8v20a10 10 0 0 1-10 10H28z" fill="#e8531f"/>
  </svg>
  <h3>Etiam euurna</h3>
  <p>Class aptent taciti sociosqu ad litora torquent per conubia nostra, per inceptos hymenaeos Proin nulla arcu</p>
  <span class="btn-read">Read More</span>
</div>

<h2 class="section-title" style="top:1118px;font-size:26px">As Featured In</h2>
<div class="featured-row">
  <span class="featured-badge"></span><span class="featured-badge"></span><span class="featured-badge"></span><span class="featured-badge"></span><span class="featured-badge"></span>
</div>
<div class="divider" style="top:1245px"></div>

<section class="about">
  <h2>About Our Company</h2>
  <p class="lead">Ridiculus mus In iaculis facilisis massa Etiam eu urna Sed porta Suspend­isse quam leo molestie sed luctus quis feugiat in pede</p>
  <p>Fusce tellus Sed metus augue convallis et vehicula ut pulvinar eu ante Integer orci tellus tristique vitae consequat nec porta vel lectus Nulla sit</p>
  <p>Phasellus felis dolor scelerisque a tempus eget lobortis id libero Aliquam nec erat at purus cursus interdum Vestibulum ligula augue bibendum accumsan vestibulum ut commodo a mi Morbi ornare gravida elit Integer congue augue et malesuada iaculis ipsum dui aliquet felis at cursus magna nisl nec elit Vestibulum gravida</p>
</section>
<span class="btn-start">Get Started</span>

<h2 class="video-title">Wach Our Video</h2>
<div class="video" role="img" aria-label="Video still of business people meeting around a laptop">
  <svg width="433" height="264" viewBox="0 0 433 264">
    <path d="M192 96v60l50-30z" fill="#fff" opacity=".9"/>
    <rect x="20" y="232" width="400" height="4" fill="#111"/>
    <circle cx="52" cy="234" r="11" fill="#111"/>
    <circle cx="52" cy="234" r="8" fill="#fff"/>
    <path d="M49 229v10l8-5z" fill="#111"/>
  </svg>
</div>
<div class="divider" style="top:1680px"></div>

<h2 class="section-title" style="top:1726px;color:var(--teal)">What Our Customer Say</h2>

<div class="testimonial" style="left:59px">
  <div class="avatar" role="img" aria-label="Customer portrait"></div>
  <p class="quote">Aliquam nec erat at purus cursus interdum Vestibulum ligula augue bibendum accumsan vestibulum ut commodo a mi Morbi ornare gravida elit Integer congue augue et malesuada iaculis ipsum dui aliquet felis at cursus</p>
  <p class="author">By Author Name</p>
</div>
<div class="testimonial" style="left:601px">
  <div class="avatar" role="img" aria-label="Customer portrait"></div>
  <p class="quote">Aliquam nec erat at purus cursus interdum Vestibulum ligula augue bibendum accumsan vestibulum ut commodo a mi Morbi ornare gravida elit Integer congue augue et malesuada iaculis ipsum dui aliquet felis</p>
  <p class="author">By Author Name</p>
</div>

<footer class="site-footer">
  <div class="footer-col" style="left:90px"><h4>Company</h4><ul><li>Cum sociis</li><li>Natoque penatibus</li><li>Magnis dis parturient</li><li>Montes nascetur</li><li>Ridiculus mus</li></ul></div>
  <div class="footer-col" style="left:286px"><h4>How it Works</h4><ul><li>Services Provide</li><li>Natoque penatibus</li><li>Montes nascetur</li><li>Ridiculus mus</li></ul></div>
  <div class="footer-col" style="left:493px"><h4>Resources</h4><ul><li>Customer Service</li><li>Legal</li><li>Sitemap</li><li>Resources</li><li>Testimonials</li></ul></div>
  <div class="footer-col" style="left:678px"><h4>Help &amp; Support</h4><ul><li>For Prospective Customers</li><li>For Current Customers</li><li>Customer Support</li><li>FAQ</li></ul></div>
  <div class="footer-col" style="left:923px"><h4>Get in Touch</h4><p class="note">Please connect with us on these</p><div class="social"><span></span><span></span><span></span><span></span></div></div>
  <p class="copyright">© 2014 Company Name.&nbsp; All right reserved.&nbsp; Term of Use</p>
</footer>

</body>
</html>
```